Lantern Above the Harbor ~ An Unbinding Passage for Versemakers

My book is called “Lantern Above the Harbor.” Its subtitle is “An Unbinding Passage for Versemakers.” It is a book about being a poet, writing poetry, and the ways in which poets are connected to both society and the central energy of the Universe. I want the cover design to be abstract and impressionistic. A suggestion of fireworks or a starburst would be a plus. To be consistent with the 3 other books I have published, I want the font for the title, as well as my name (Dorothea Halvik) to be Papyrus. The subtitle font can be something more plain and sans serif, like Arial or Franklin Gothic Book, probably in italics. As for color, I definitely want pale gold (angelic). Possible other complimentary colors could be either light or dark shades of gray, turquoise, rose, rust or red. I'm attaching the back cover text and also three pages from inside the book that have line drawings, to give an example of the interior artwork.
Updates

Forgot to mention: My book is a paperback. Its size will be 8.5" high and 5.5" wide. I'm self-publishing it, and it will be printed by Quillby Press in Nebraska, USA. It has 104 pages. I think you need the number of pages, in order to make the spine of the book the correct width.

Target Market(s)

My target market is people who write poetry or are interested in how poetry is written.

Industry/Entity Type

Poetry

Font styles to use
Sans Serif
Other font styles liked:
• Papyrus for the front cover. Arial or another sans serif font on the back cover.

Colors

Designer to choose colors to be used in the design.

Requirements
Must have
• My book cover needs to be inspiring and uplifting, as well as abstract and impressionistic, with kind of a "New Age" feel. I don't want anything that looks rigid and scholarly.
Nice to have
• The book talks about the connection poets have to the Universe and the Creative Energy at the center of everything. The cover should convey that Energy.
Should not have
• My cover should not be realistic, logical or straight-laced. I want something that feels free, imaginative and unfettered.

```html
<!DOCTYPE html>
<html lang="en">
<head>
<meta charset="utf-8">
<title>Lantern Above the Harbor — Cover Spread</title>
<link href="https://fonts.googleapis.com/css2?family=Macondo&family=Libre+Franklin:ital,wght@0,400;0,600;1,400;1,600&family=Arimo:ital@1&display=swap" rel="stylesheet">
<style>
  :root {
    --paper: #ffffff;
    --cover-bronze: #9c7036;
    --title-gold: #f7ea2c;
    --title-white: #ffffff;
    --rule-gold: #d9c75e;
    --ink-dark: #141008;
    --burst-core: #e8c9a6;
    --burst-glow: #f0a24e;
    --burst-rose: #d99a88;
  }
  * { margin: 0; padding: 0; box-sizing: border-box; }
  html, body { width: 1200px; height: 900px; overflow: hidden; background: var(--paper); }
  .spread { position: relative; width: 1200px; height: 900px; background: var(--paper); }
  .cover {
    position: absolute; left: 25px; top: 25px; width: 1150px; height: 850px;
    background: var(--cover-bronze); overflow: hidden;
  }
  .energy-burst { position: absolute; left: 580px; top: 0; width: 570px; height: 850px; }

  /* back cover */
  .back-copy {
    position: absolute; left: 59px; top: 44px; width: 430px;
    font-family: "Libre Franklin", sans-serif; font-size: 14px; line-height: 19.4px;
    letter-spacing: -0.3px; word-spacing: -0.5px;
    color: var(--title-white); text-align: justify;
  }
  .back-copy p { margin-bottom: 19.4px; }
  .back-copy .book-name { font-weight: 600; font-style: italic; }
  .back-copy .chapter-intro { margin-bottom: 0; text-align: left; }
  .back-copy .chapters { text-align: center; }
  .author-photo {
    float: right; width: 89px; height: 126px; margin: 0 0 6px 12px;
    background: linear-gradient(160deg, #8a7a66, #d9c4b2 55%, #3f7a5e);
  }
  .barcode-space {
    position: absolute; left: 149px; top: 642px; width: 236px; height: 138px; background: var(--paper);
  }

  /* spine */
  .spine-title, .spine-author {
    position: absolute; writing-mode: vertical-rl; color: var(--title-white);
    font-family: "Macondo", fantasy; white-space: nowrap;
  }
  .spine-title { left: 563px; top: 36px; font-size: 25px; letter-spacing: 4.5px; }
  .spine-author { left: 567px; top: 578px; font-size: 16px; letter-spacing: 1.5px; }

  /* front cover */
  .front-title {
    position: absolute; left: 660px; top: 36px; width: 460px; text-align: center;
    font-family: "Macondo", fantasy; font-weight: 400; line-height: 1; text-transform: uppercase;
  }
  .front-title .lead { display: block; color: var(--title-gold); font-size: 92px; letter-spacing: -1px; }
  .front-title .mid { display: block; color: var(--title-white); font-size: 46px; margin-top: 4px; }
  .front-title .tail { display: block; color: var(--title-white); font-size: 76px; margin-top: 2px; }
  .subtitle {
    position: absolute; left: 720px; top: 512px; width: 330px; text-align: center;
    font-family: "Arimo", sans-serif; font-style: italic; font-size: 24px;
    line-height: 29.5px; letter-spacing: 4px; color: var(--ink-dark);
  }
  .front-author {
    position: absolute; left: 722px; top: 790px; width: 310px; text-align: center;
    font-family: "Macondo", fantasy; font-size: 36px; color: var(--title-white); line-height: 1;
  }
  .base-rule { position: absolute; top: 810px; height: 1px; background: var(--rule-gold); }
  .base-rule.left { left: 0; width: 718px; }
  .base-rule.right { left: 1033px; width: 117px; }
</style>
</head>
<body>
<div class="spread">
  <div class="cover">
    <svg class="energy-burst" role="img" aria-label="Abstract starburst of radiating light streaks with a glowing winged figure at the centre" viewBox="0 0 570 850">
      <defs>
        <radialGradient id="burstGlow" cx="0.57" cy="0.62" r="0.7">
          <stop offset="0" stop-color="var(--burst-core)"/>
          <stop offset="0.25" stop-color="var(--burst-rose)" stop-opacity="0.9"/>
          <stop offset="0.5" stop-color="var(--burst-glow)" stop-opacity="0.55"/>
          <stop offset="1" stop-color="var(--cover-bronze)" stop-opacity="0"/>
        </radialGradient>
      </defs>
      <rect width="570" height="850" fill="url(#burstGlow)"/>
    </svg>

    <div class="back-copy">
      <p><span class="author-photo" role="img" aria-label="Author portrait"></span><span class="book-name">Lantern Above the Harbor</span> is indeed “An Unbinding Passage for Versemakers.” It is written by Dorothea Halvik, an exciting, imaginative voice in American poetry.</p>
      <p>In <span class="book-name">Lantern Above the Harbor,</span> Dorothea discusses the essential elements of poetry and the process of writing it. She offers an inspiring view of the mission of poets and their connection to both society and the larger forces in the Universe. Her book is motivational, refreshing and irrepressibly optimistic.</p>
      <p class="chapter-intro">The seven intriguing chapters in <em>Lantern Above the Harbor</em> are</p>
      <p class="chapters">LIBERATION ~ EXPERIENCE ~ WORDS ~ POETRY ~<br>INTEGRITY ~ BEAUTY ~ CREATION</p>
      <p>For over 50 years, Dorothea has been a teacher of writing and poetry. Since 2007, she has published three books of her poems: <em>Mind the Kettle Spout, The Pale Hem of Ever</em> and <em>The Wide Velvet Hush</em>. Her work overflows with her characteristically rich images and quirky metaphors. It runs the gamut from subtle eroticism to abject grief, from defiant rage to philosophical meditation, and from borderline blasphemy to lyrical fantasy.</p>
      <p>Dorothea has been called by critic Thaddeus Wrenfield “a poet to be reckoned with; bright, feisty, compassionate.” (<em>The Dusk Courier,</em> Millbrook, PA). Author Ione Castellow (<em>“Larkhollow,”</em> 2011) says Dorothea’s poetry is like “a perpetual Surprise Party ~ memorable, insightful and thematically fascinating.”</p>
    </div>
    <div class="barcode-space"></div>

    <div class="spine-title">LANTERN ABOVE THE HARBOR</div>
    <div class="spine-author">DOROTHEA HALVIK</div>

    <h1 class="front-title">
      <span class="lead">Lantern</span>
      <span class="mid">Above the</span>
      <span class="tail">Harbor</span>
    </h1>
    <p class="subtitle">An<br>Unbinding<br>Passage for<br>Versemakers</p>

    <div class="base-rule left"></div>
    <div class="base-rule right"></div>
    <p class="front-author">Dorothea Halvik</p>
  </div>
</div>
</body>
</html>
```